Tallowind Power - Company Brochure / Display Folder / DL Flyer

We are a trader in environmental commodities based in Australia and require the following 4 designs for an upcoming exhibition;
1) Brochure Folder
Essentially this will be a presentation folder for a number of A4 sheets and will allow us to present business cards. We would like it based on the same design as our stand background - please see attached (001) for reference.
I have attached a file (002) that is basically what i am after, if you could recreate this or something similar it be sufficient. Please change the blue lines to green and incorporate an image that represents solar / environment / renewable energy etc.
Please include our logo (003) as well as the words 'experts in environmental commodity trading'
The back of the folder should have our address, contact number, homepage etc - please refer to the website for these details www.tallowindpower.com.au.
The template is included also, please ensure the deisgn fits within these boundaries for printing (004 / Forme 8)
2) A4 Flyer
We are after a re design of an old flyer that highlights what we do as a business. I have included the wording for this (005) but am open to interpretations as to designs. Please keep it relevant to the graphics requested for the presentation folder.
This will be a single page A4 sheet - very easy.
3) DL Brochure
We will be running a promotion at the exhibition for cash rewards and need a double sided DL flyer designed so the can be handed out. The back of the flyer should have our logo as well as the green graphics consistent with the stand design / background while the front needs to highlight the following promotional offer;
Tallowind Power Cash Rewards Offer
Get more out of your STC's -trade with us to receive instant cash back!
Trade 1000 STC - receive $250 cash rewards card
Trade 5000 STC - receive $500 cash rewards card
(x1 card on the first 1000 + x2 more cards on the first 5000)
Cash rewards cards are valid everywhere that accepts eftpos - cash can even be withdrawn at ATMS!
Offer valid until October 31st 2014
Unregistered Trade Only.
Please keep this text to the left and incorporate an image or graphic on the right side. One that is professional, ties in with the notion of environmental trading but highlights the offer.
Again we open to interpretations with this one.
4) Card Design
Very basic - a design is needed for the rewards card mentioned in the promotion above. I have attached the template / outline required for this (006/ 007) and basically need out logo and a bit of colour on the cash card.
We are open to some ideas but the main thing is being consistent with the stand design that we will be exhibiting in. We like the graphics used and the plain white with the green curved concept. Please ensure the greens from our logo also.
I will do my best to answer any queries you may have, the files should have all the info needed to get started and we usually have a few design amendments after the first drafts are sent through.
Apologies about the timeframe with this one - we are looking to move fast so the earlier submissions will be considered as I can work back and forth with them.
Good Luck
Tallowind Power.

```html
<!DOCTYPE html>
<html lang="en">
<head>
<meta charset="utf-8">
<title>Tallowind Power – Presentation Folder</title>
<link rel="stylesheet" href="https://fonts.googleapis.com/css2?family=Play:wght@700&family=Hind:wght@400;500&display=swap">
<style>
  :root {
    --paper: #ffffff;
    --green-deep: #1f8a3c;
    --green-brand: #2aa84a;
    --green-bright: #7ccf1e;
    --green-lime: #b8e24a;
    --green-pale: #e4f5a6;
    --photo-top: #3c7cc6;
    --photo-low: #6fa3d8;
    --ink: #2c2c2c;
  }
  * { margin: 0; padding: 0; box-sizing: border-box; }
  html, body { width: 848px; height: 1200px; overflow: hidden; background: var(--paper); }
  .folder-cover {
    position: relative;
    width: 848px;
    height: 1200px;
    background: var(--paper);
    overflow: hidden;
    font-family: "Hind", sans-serif;
  }
  .swirl { position: absolute; inset: 0; width: 848px; height: 1200px; }
  .brand-block { position: absolute; left: 58px; top: 870px; }
  .brand-name {
    display: flex;
    align-items: center;
    gap: 16px;
    font-family: "Play", sans-serif;
    font-weight: 700;
    font-size: 46px;
    line-height: 56px;
    color: var(--green-deep);
    letter-spacing: 0.5px;
  }
  .brand-mark { width: 56px; height: 56px; background: var(--green-bright); }
  .tagline {
    margin-top: 36px;
    font-size: 25px;
    line-height: 36px;
    font-weight: 500;
    color: var(--green-brand);
  }
  .contact-list { list-style: none; margin-top: 22px; }
  .contact-item {
    display: flex;
    align-items: center;
    gap: 14px;
    font-size: 17px;
    color: var(--ink);
    height: 27px;
  }
  .contact-icon { width: 16px; height: 16px; fill: var(--ink); flex: none; }
</style>
</head>
<body>
<main class="folder-cover">
  <svg class="swirl" viewBox="0 0 848 1200" aria-hidden="true">
    <defs>
      <linearGradient id="band-fill" x1="0" y1="0" x2="1" y2="1">
        <stop offset="0" stop-color="#d9f07a"/>
        <stop offset="0.45" stop-color="#c4e85a"/>
        <stop offset="1" stop-color="#eef8b8"/>
      </linearGradient>
      <linearGradient id="photo-fill" x1="0" y1="0" x2="0" y2="1">
        <stop offset="0" stop-color="var(--photo-top)"/>
        <stop offset="1" stop-color="var(--photo-low)"/>
      </linearGradient>
    </defs>
    <path class="swirl-body" fill="url(#band-fill)"
      d="M0,0 H848 V1200 H620 C610,1050 600,930 580,860 C555,760 520,720 440,690 C300,640 120,560 0,456 Z"/>
    <path fill="none" stroke="var(--green-bright)" stroke-width="26" opacity="0.55"
      d="M0,120 C220,40 520,20 848,90"/>
    <path fill="none" stroke="var(--green-deep)" stroke-width="6" opacity="0.7"
      d="M0,250 C180,120 480,80 848,150"/>
    <path fill="none" stroke="var(--green-bright)" stroke-width="34" opacity="0.6"
      d="M0,330 C80,230 200,190 330,190"/>
    <path fill="none" stroke="var(--green-deep)" stroke-width="5" opacity="0.6"
      d="M0,420 C120,540 260,610 380,650 C480,685 540,720 565,830 C585,930 595,1060 610,1200"/>
    <path fill="none" stroke="var(--green-lime)" stroke-width="30" opacity="0.6"
      d="M40,480 C180,600 320,650 440,690 C540,725 580,790 600,900 C615,1000 625,1110 650,1200"/>
    <path fill="none" stroke="#ffffff" stroke-width="10" opacity="0.5"
      d="M0,180 C200,90 520,60 848,120"/>
    <path fill="none" stroke="var(--green-bright)" stroke-width="14" opacity="0.5"
      d="M260,480 C420,560 640,600 848,620"/>
    <path class="energy-photo" role="img"
      aria-label="Photo of wind turbines and solar panels under a blue sky"
      fill="url(#photo-fill)"
      d="M430,210 C600,195 760,190 848,195 L848,575 C700,540 500,470 310,415 C300,330 360,230 430,210 Z"/>
  </svg>

  <section class="brand-block">
    <div class="brand-name"><span class="brand-mark"></span>Tallowind Power</div>
    <p class="tagline">experts in environmental commodity trading</p>
    <ul class="contact-list">
      <li class="contact-item">
        <svg class="contact-icon" viewBox="0 0 16 16"><path d="M8 1 L15 8 H13 V15 H9.5 V10.5 H6.5 V15 H3 V8 H1 Z"/></svg>
        Level 14 82 Harlow Street, Melbourne 3000 VIC
      </li>
      <li class="contact-item">
        <svg class="contact-icon" viewBox="0 0 16 16"><path d="M1 5 C1 3 4 2 8 2 C12 2 15 3 15 5 V6.5 H11.5 V5 H4.5 V6.5 H1 Z M3 8 H13 L14 14 H2 Z"/></svg>
        1300 418 262
      </li>
      <li class="contact-item">
        <svg class="contact-icon" viewBox="0 0 16 16"><circle cx="8" cy="8" r="7"/><path d="M1 8 H15 M8 1 C5 4 5 12 8 15 M8 1 C11 4 11 12 8 15" stroke="#fff" stroke-width="1.1" fill="none"/></svg>
        www.tallowindpower.com.au
      </li>
    </ul>
  </section>
</main>
</body>
</html>
```